PROMOTION CARD for NEW APPLICATION LAUNCH

Hi need double sided promotion card the size of a postcard.
we car launching a new app, and need to promote
the app is focused on the automotive
the functions are to help remind customers when there car utilities bills are due.
* registration
*Insurance
*CTP due
*Service
* Warranty

Helps sell your car under the ( "Whats New " Button )
Helps you find a better finance or insurance deal.( Zenqa Portal)

Target Market(s)

All consumers who own a Car all ages both male and female

Industry/Entity Type

Automotive

Font styles to use
Sans Serif

Colors
0293ce
9ccb3b
fffbf0

Requirements
Must have
• clean and professional makes you want to down load the app
Nice to have
• clear description about what the app dose feature and functions
• the application will reminder the customer when the
• *registration due
• * insurance due
• *Finance due
• Kelvra picture
• car or road in background
• *CTP due
• *Service due
• *Warranty Due
• it will also pay a payment function so you can pay,
Should not have
• color brown/ no running writing

```html
<!DOCTYPE html>
<html lang="en">
<head>
<meta charset="utf-8">
<title>Drivora App – Promotion Card</title>
<link href="https://fonts.googleapis.com/css2?family=Mulish:wght@400;600;700;800&display=swap" rel="stylesheet">
<style>
  :root{
    --stage:#2a5daa;
    --blue:#0293ce;
    --green:#9ccb3b;
    --teal:#0f86b0;
    --ink:#111111;
    --body:#2a2a2a;
    --card-front:#f4f5f5;
    --card-back:#eef0ef;
    --white:#ffffff;
  }
  *{box-sizing:border-box;margin:0;padding:0}
  html,body{width:1200px;height:1000px;overflow:hidden}
  body{background:var(--stage);font-family:"Mulish",sans-serif;color:var(--body);position:relative}

  .card{position:absolute;overflow:hidden}
  .card--front{left:118px;top:34px;width:692px;height:447px;background:var(--card-front)}
  .card--back{left:389px;top:498px;width:703px;height:447px;background:var(--card-back)}

  .street-photo{position:absolute;inset:0;
    background:linear-gradient(100deg,#c9cccf 0%,#dfe1e2 35%,#eef0f0 60%,#f6f7f7 100%);opacity:.9}

  .brand-panel{position:absolute;left:45px;top:34px;width:258px;height:381px;border-radius:12px;
    background:linear-gradient(180deg,#8fc63c 0%,#5cb36a 35%,#1f97ad 70%,#0f86b8 100%);opacity:.93}
  .brand-box{position:absolute;left:44px;top:51px;width:164px;height:174px;border:1.5px solid var(--ink);border-radius:12px;
    display:flex;flex-direction:column;align-items:center;justify-content:center;gap:14px}
  .brand-box__mark{width:60px;height:60px;background:var(--blue);border-radius:6px}
  .brand-box__name{font-size:34px;font-weight:600;color:var(--ink);letter-spacing:.5px}
  .brand-panel__title{position:absolute;left:0;right:0;top:236px;text-align:center;font-size:40px;font-weight:800;color:var(--ink)}
  .brand-panel__tagline{position:absolute;left:0;right:0;top:290px;text-align:center;font-size:24px;line-height:29px;color:var(--ink)}

  .front-headline{position:absolute;left:323px;top:70px;font-size:24px;font-weight:700;color:var(--ink)}
  .reminders{position:absolute;list-style:none;font-size:14px;color:var(--ink)}
  .reminders li{position:relative;padding-left:20px;height:36px}
  .reminders li::before{content:"";position:absolute;left:0;top:2px;width:13px;height:13px;border-radius:50%}
  .reminders--blue{left:329px;top:139px}
  .reminders--blue li::before{background:var(--blue)}
  .reminders--green{left:503px;top:138px}
  .reminders--green li::before{background:var(--green)}

  .pill{position:absolute;border-radius:8px;display:flex;align-items:center;justify-content:center;font-size:16px;color:var(--ink)}
  .pill--blue{left:318px;top:267px;width:155px;height:39px;background:var(--blue)}
  .pill--green{left:493px;top:267px;width:155px;height:39px;background:var(--green)}
  .pill-caption{position:absolute;font-size:13px;line-height:19px;color:var(--ink)}
  .pill-caption--left{left:321px;top:318px}
  .pill-caption--right{left:493px;top:318px;width:160px}

  .feature-btn{position:absolute;height:52px;border-radius:8px;background:var(--green);
    display:flex;align-items:center;padding-left:36px;font-size:19px;font-weight:800;color:var(--ink)}
  .feature-btn__brand{position:absolute;right:20px;top:9px;display:flex;flex-direction:column;align-items:center;gap:2px;font-size:11px;font-weight:700}
  .feature-btn__brand span{width:22px;height:22px;background:var(--blue);border-radius:3px}
  .feature-btn--portal{left:39px;top:39px;width:262px}
  .feature-btn--news{left:36px;top:219px;width:267px;padding-left:55px}
  .feature-text{position:absolute;left:38px;width:272px;font-size:13.5px;line-height:19px;color:var(--ink)}
  .feature-text--portal{top:104px}
  .feature-text--news{top:284px}
  .phone-line{position:absolute;left:37px;top:388px;font-size:16px;color:var(--ink)}

  .divider{position:absolute;left:333px;top:39px;width:2px;height:367px;background:var(--green)}

  .info{position:absolute;left:357px;top:40px;width:320px;color:var(--ink)}
  .info h2{font-size:16px;font-weight:700;margin-bottom:19px}
  .info h3{font-size:16px;font-weight:700;margin-top:20px}
  .info p{font-size:13.5px;line-height:19px}
  .info p + p{margin-top:19px}
  .download-btn{position:absolute;left:359px;top:327px;width:288px;height:52px;border-radius:10px;
    background:linear-gradient(90deg,var(--green) 0%,#3fae8a 35%,var(--blue) 70%,#0f6f9e 100%);
    display:flex;align-items:center;justify-content:center;font-size:27px;font-weight:800;color:var(--green);letter-spacing:.3px}
  .web{position:absolute;left:362px;top:389px;font-size:16px;color:var(--ink)}
</style>
</head>
<body>

<section class="card card--front" aria-label="Front of promotion card">
  <div class="street-photo" role="img" aria-label="Faded photo of a car parked on a city street"></div>

  <div class="brand-panel">
    <div class="brand-box">
      <span class="brand-box__mark"></span>
      <span class="brand-box__name">drivora</span>
    </div>
    <div class="brand-panel__title">App</div>
    <p class="brand-panel__tagline">We remember what<br>You forget!</p>
  </div>

  <h1 class="front-headline">An app that will remind you</h1>
  <ul class="reminders reminders--blue">
    <li>Registration Due</li>
    <li>Insurance Due</li>
    <li>Finance Due</li>
  </ul>
  <ul class="reminders reminders--green">
    <li>CTP Due</li>
    <li>Service Due</li>
    <li>Warranty Due</li>
  </ul>

  <div class="pill pill--blue">Zenqa Portal</div>
  <div class="pill pill--green">What’s New</div>
  <p class="pill-caption pill-caption--left">Helps sell your car</p>
  <p class="pill-caption pill-caption--right">Helps you find a better finance or insurance deal.</p>
</section>

<section class="card card--back" aria-label="Back of promotion card">
  <div class="feature-btn feature-btn--portal">Zenqa Portal
    <div class="feature-btn__brand"><span></span>drivora</div>
  </div>
  <p class="feature-text feature-text--portal">“<b>Zenqa Portal</b>” button helps customers find a more competitive deal, insurance or finance, or car provide a valuation.</p>

  <div class="feature-btn feature-btn--news">What’s New
    <div class="feature-btn__brand"><span></span>drivora</div>
  </div>
  <p class="feature-text feature-text--news">“<b>What’s New</b>” button allows customers to buy and sell automotive products, sush as car parts or sell their cars or see new promotion owners with auto traders.</p>
  <p class="phone-line">1300 555 019 and 1300 5 drivora</p>

  <div class="divider"></div>

  <div class="info">
    <h2>Available to all Smart phone users</h2>
    <p>Drivora app is a collection of online services to enhance your owenership of a motor vehicle.</p>
    <h3>Drivora Features:</h3>
    <p>Vehicle Data and receipt box storage</p>
    <p>Contact details for all vehicle contracts Registration, Insurance, Car ServiceCTP, Warrenty, Roadside, Tolls &amp; fires, Calendar reminders, with direct Payments options for your vehicle utility bills, much more.</p>
  </div>

  <div class="download-btn">Free Download</div>
  <p class="web">www.drivora.net.au</p>
</section>

</body>
</html>
```